TBrenwick Business Cards & Letterhead

I have a logo but need a design for some new business cards. We are a Design-Build Firm that specializes in the design and construction of commercial projects.
the cards need to be professional. no cartoon stuff.
i would like to have the cards in AI format so I can update the card as needed. Logo is provided.
Our Address is: 4718 Fenmoor Ct. Carrow, Vermont 05412

```html
<!DOCTYPE html>
<html lang="en">
<head>
<meta charset="utf-8">
<title>TBrenwick Business Card</title>
<link href="https://fonts.googleapis.com/css2?family=Montserrat:wght@400;600;700&display=swap" rel="stylesheet">
<style>
  :root {
    --backdrop: #3b3b3d;
    --card: #1d1a1e;
    --ink: #ffffff;
    --ink-soft: #e6e6e8;
    --brand-blue: #0f6fae;
    --brand-blue-light: #1b84c4;
    --brand-blue-dark: #0b5a92;
  }
  * { margin: 0; padding: 0; box-sizing: border-box; }
  html, body {
    width: 1200px; height: 900px; overflow: hidden;
    background: var(--backdrop);
    font-family: "Montserrat", Arial, sans-serif;
  }
  .canvas { position: relative; width: 1200px; height: 900px; }
  .card {
    position: absolute; top: 192px;
    width: 298px; height: 515px;
    background: var(--card);
    box-shadow: 0 4px 14px rgba(0,0,0,.35);
    color: var(--ink);
    overflow: hidden;
  }
  .card--front { left: 260px; }
  .card--back { left: 644px; }

  .wordmark { display: flex; align-items: center; gap: 7px; }
  .wordmark__square { width: 18px; height: 18px; background: var(--brand-blue); }
  .wordmark__name { font-weight: 700; color: var(--ink); letter-spacing: .5px; line-height: 1; }
  .tagline { font-size: 8px; font-weight: 400; color: var(--ink-soft); letter-spacing: .2px; }

  .front-lockup {
    position: absolute; top: 322px; left: 0; width: 100%;
    display: flex; flex-direction: column; align-items: center; gap: 4px;
  }
  .front-lockup .wordmark__name { font-size: 25px; }
  .front-lockup .wordmark__square { width: 22px; height: 22px; }

  .back-lockup { position: absolute; top: 42px; left: 40px; }
  .back-lockup .wordmark__name { font-size: 23px; }
  .back-lockup .tagline { margin-left: 25px; margin-top: 2px; }

  .person { position: absolute; top: 276px; left: 40px; }
  .person__name { font-size: 16px; font-weight: 600; letter-spacing: .3px; }
  .person__role { font-size: 13.5px; font-weight: 600; margin-top: 2px; }

  .divider { position: absolute; top: 338px; left: 40px; width: 37px; height: 2px; background: var(--ink); }

  .address { position: absolute; top: 374px; left: 40px; font-size: 10px; font-weight: 600; line-height: 1.15; }

  .contacts { position: absolute; top: 410px; left: 40px; list-style: none; font-size: 14px; font-weight: 600; line-height: 1.25; }
  .contacts li { display: flex; align-items: center; gap: 6px; }
  .contacts svg { width: 11px; height: 11px; flex: none; }

  .web-band {
    position: absolute; left: 0; bottom: 0; width: 100%; height: 52px;
    background: linear-gradient(90deg, var(--brand-blue-dark), var(--brand-blue-light));
    display: flex; align-items: center; padding-left: 40px;
    font-size: 14px; font-weight: 600;
  }
</style>
</head>
<body>
<main class="canvas">
  <section class="card card--front" aria-label="Card front">
    <div class="front-lockup">
      <div class="wordmark">
        <span class="wordmark__square"></span>
        <span class="wordmark__name">BRENWICK</span>
      </div>
      <p class="tagline">THE BUILDING &amp; DEVELOPMENT CO.</p>
    </div>
  </section>

  <section class="card card--back" aria-label="Card back">
    <div class="back-lockup">
      <div class="wordmark">
        <span class="wordmark__square"></span>
        <span class="wordmark__name">BRENWICK</span>
      </div>
      <p class="tagline">THE BUILDING &amp; DEVELOPMENT CO.</p>
    </div>

    <div class="person">
      <p class="person__name">MARCUS HALE</p>
      <p class="person__role">managing director</p>
    </div>

    <div class="divider"></div>

    <p class="address">4718 Fenmoor Ct. Carrow<br>Vermont 05412</p>

    <ul class="contacts">
      <li>
        <svg viewBox="0 0 12 12" aria-hidden="true"><path fill="#1b84c4" d="M1 4c0-2 2-3 5-3s5 1 5 3l-2 1-1-2H4L3 5 1 4zm2 2h6l1 4H2l1-4zm3 1a1.2 1.2 0 100 2.4A1.2 1.2 0 006 7z"/></svg>
        5550 123 456
      </li>
      <li>
        <svg viewBox="0 0 12 12" aria-hidden="true"><rect x="1" y="3" width="10" height="7" fill="#1b84c4"/><path d="M1 3l5 4 5-4" fill="none" stroke="#1d1a1e" stroke-width="1"/></svg>
        m.hale@tbrenwick.com
      </li>
    </ul>

    <div class="web-band">www.tbrenwick.com</div>
  </section>
</main>
</body>
</html>
```